Keystone Prime Water Tank

I primarily market the water tanks so want a business care that reflects that. I have attached the water tank logo. You have been working on our water tank so maybe we can use that on the card et. I am leaving as one sided but can be double sided if that works. The information that needs to be on the cards is as follows: Gerald T. Munro Phone numbers: Office 555-284-9137 Direct 555-619-2405 Mobile 555-372-5841 email address: gerald@fieldgearworks.com Address P.O. Box 8273 Ridgeford, ST 30512 Web Page: www.fieldgearworks.com. A lot to fit on the card. Thanks

```html
<!DOCTYPE html>
<html lang="en">
<head>
<meta charset="utf-8">
<title>Keystone Prime Water Tank – Business Card</title>
<link href="https://fonts.googleapis.com/css2?family=Source+Sans+3:wght@400;700;900&display=swap" rel="stylesheet">
<style>
  :root{
    --page:#f4f4f4;
    --ink:#1c1c1c;
    --red:#d71f26;
    --paper-light:#f6f6f6;
    --paper-dark:#e3e3e3;
    --text:#1e1e1e;
    --white:#f2f2f2;
  }
  *{box-sizing:border-box;margin:0;padding:0}
  html,body{width:1200px;height:960px;overflow:hidden;background:var(--page)}
  body{position:relative;font-family:"Source Sans 3",Arial,sans-serif;color:var(--text)}

  .card{position:absolute;left:284px;width:632px;overflow:hidden}
  .card-front{top:100px;height:360px;background:var(--ink)}
  .card-back{top:500px;height:362px;background:linear-gradient(90deg,var(--paper-light),var(--paper-dark))}

  .decor{position:absolute;background:var(--red)}
  .card-front .decor{left:0;top:0;width:246px;height:360px;clip-path:polygon(0 0,3% 0,20% 14%,100% 100%,0 100%)}
  .card-back .decor{left:386px;top:0;width:246px;height:362px;clip-path:polygon(100% 0,100% 100%,0 100%)}

  .brand-name{font-weight:900;text-transform:uppercase;line-height:1;letter-spacing:.5px;white-space:nowrap}
  .card-front .brand-name{position:absolute;left:308px;top:216px;width:266px;color:var(--white);font-size:31px;text-align:center}
  .card-back .brand-name{position:absolute;left:46px;top:38px;color:var(--ink);font-size:25px}

  .edge-strip{position:absolute;left:0;top:0;width:14px;height:100%;background:var(--ink)}
  .edge-accent{position:absolute;left:0;top:130px;width:14px;height:38px;background:var(--red)}

  .person{position:absolute;left:46px;top:128px}
  .person-name{color:var(--red);font-weight:700;font-size:20px;line-height:24px}
  .person-role{font-size:16px;line-height:20px}

  .contacts{position:absolute;left:46px;top:198px;list-style:none;font-size:16px;line-height:21px}
  .contacts li{display:flex;align-items:center;gap:5px}
  .contacts svg{width:14px;height:14px;flex:none}
  .address{position:absolute;left:46px;top:312px;font-size:16px;line-height:20px}
</style>
</head>
<body>

<section class="card card-front" aria-label="Card front">
  <div class="decor" role="img" aria-label="Red angled stripe decoration"></div>
  <p class="brand-name">Keystone Prime<br>Water Tank</p>
</section>

<section class="card card-back" aria-label="Card back">
  <div class="edge-strip"></div>
  <div class="edge-accent"></div>
  <div class="decor" role="img" aria-label="Red angled stripe decoration"></div>
  <p class="brand-name">Keystone Prime<br>Water Tank</p>

  <div class="person">
    <p class="person-name">Gerald T. Munro</p>
    <p class="person-role">Founder</p>
  </div>

  <ul class="contacts">
    <li><svg viewBox="0 0 16 16" fill="none" stroke="#d71f26" stroke-width="1.6"><path d="M3 2l3 0 1 3-2 1.5a8 8 0 0 0 4.5 4.5L11 9l3 1v3a1 1 0 0 1-1 1A12 12 0 0 1 2 3a1 1 0 0 1 1-1z"/></svg>555-284-9137</li>
    <li><svg viewBox="0 0 16 16" fill="none" stroke="#d71f26" stroke-width="1.6"><path d="M3 2l3 0 1 3-2 1.5a8 8 0 0 0 4.5 4.5L11 9l3 1v3a1 1 0 0 1-1 1A12 12 0 0 1 2 3a1 1 0 0 1 1-1z"/></svg>555-619-2405 Direct</li>
    <li><svg viewBox="0 0 16 16" fill="none" stroke="#d71f26" stroke-width="1.6"><rect x="4" y="1.5" width="8" height="13" rx="1.5"/><path d="M7 12.5h2"/></svg>555-372-5841</li>
    <li><svg viewBox="0 0 16 16" fill="none" stroke="#d71f26" stroke-width="1.6"><rect x="1.5" y="3.5" width="13" height="9"/><path d="M1.5 3.5l6.5 5 6.5-5"/></svg>gerald@fieldgearworks.com</li>
    <li><svg viewBox="0 0 16 16" fill="none" stroke="#d71f26" stroke-width="1.3"><circle cx="8" cy="8" r="6.5"/><ellipse cx="8" cy="8" rx="3" ry="6.5"/><path d="M1.5 8h13M2.5 5h11M2.5 11h11"/></svg>www.fieldgearworks.com</li>
  </ul>

  <p class="address">P.O. Box 8273 Ridgeford, ST 30512</p>
</section>

</body>
</html>
```